Hot-air ballooning company needs a DL-size flyer

Skylark Aerial Tours is a hot-air ballooning company which flies passengers in the King Valley, Victoria, Australia.
We need a 2-sided DL-size flyer which promotes our hot-air balloon flights and packages.
Most of our customers are couples, and we want the flyer design to communicate safety, adventure, and romance.
The flyer should make the best use of our images which we provide, and we've also included a document with the text for the flyer.
Updates

2 days is not long enough to gather designs, the brief never asked me what my deadline should be.

Target Market(s)

Couples, buyers are majority female, between the ages of 20-60

Industry/Entity Type

Tourism

Font styles to use
Sans Serif

Colors

Designer to choose colors to be used in the design.

Requirements
Must have
• Communicate safety, adventure, and romance
• Use images
Nice to have
• There is a lot of text, it would be great if you could make it look like as little text as possible
Should not have
• No childish designs

```html
<!DOCTYPE html>
<html lang="en">
<head>
<meta charset="utf-8">
<title>Skylark Aerial Tours – DL Flyer</title>
<link rel="stylesheet" href="https://fonts.googleapis.com/css2?family=Oswald:wght@500&family=Lato:ital,wght@0,400;0,700;0,900;1,400;1,700&display=swap">
<style>
:root{
  --navy:#1d2a66;
  --navy-deep:#141d4d;
  --gold:#c8951c;
  --gold-light:#f1d272;
  --yellow:#f4e24a;
  --ink:#1e1e1e;
  --paper:#ffffff;
  --mist:#e9ecf2;
  --stage:#3a3a3a;
}
*{margin:0;padding:0;box-sizing:border-box}
html,body{width:1200px;height:902px;overflow:hidden;background:var(--stage)}
body{position:relative;font-family:"Lato",Arial,sans-serif;color:var(--ink)}
.flyer{position:absolute;top:64px;width:377px;height:775px;overflow:hidden;background:var(--paper)}
.flyer--front{left:195px}
.flyer--back{left:628px}
.flyer svg.art{position:absolute;inset:0;width:377px;height:775px}
.text{position:absolute;left:0;width:100%;text-align:center}
.headline{top:368px;font-family:"Oswald",Arial,sans-serif;font-weight:500;font-size:27px;color:var(--paper);letter-spacing:.2px}
.subhead{top:404px;font-family:"Oswald",Arial,sans-serif;font-weight:500;font-size:19px;line-height:25px;color:var(--yellow);letter-spacing:.4px}
.intro{top:500px;padding:0 22px;font-size:10px;line-height:12.3px}
.intro p{margin-bottom:12px}
.booking{font-weight:900;font-size:10.5px;color:var(--ink)}
.contact{font-weight:700;color:var(--paper);line-height:1.45}
.contact span::before{content:"";display:inline-block;width:7px;height:7px;border:1.3px solid var(--paper);border-radius:50%;margin-right:5px;vertical-align:0}
.social{font-weight:700;font-size:8.4px;line-height:11px}
.social .lead{color:var(--yellow)}
.front-booking{top:664px}
.front-contact{top:678px;font-size:10px}
.front-social{top:744px;color:var(--paper)}
.pill{position:absolute;left:102px;top:227px;width:165px;height:26px;border-radius:13px;background:linear-gradient(var(--gold-light),var(--gold));border:2px solid var(--paper);box-shadow:0 1px 3px rgba(0,0,0,.35);font-weight:900;font-size:14px;line-height:22px;text-align:center;color:var(--navy-deep)}
.flight-box{position:absolute;left:22px;top:240px;width:335px;height:312px;border:2px solid var(--gold);border-radius:8px}
.bullets{position:absolute;left:22px;width:335px;list-style:none;text-align:center;font-style:italic;font-size:10.6px;line-height:13.4px}
.bullets li{margin-bottom:9px}
.bullets li::before{content:"";display:inline-block;width:7px;height:7px;border-radius:50%;background:var(--gold);margin-right:6px;vertical-align:1px}
.bullets--main{top:273px;padding:0 10px}
.bullets--facts{top:419px}
.bullets--facts li{margin-bottom:4.6px}
.back-booking{top:564px;font-size:10.5px}
.back-contact{top:591px;font-size:12.5px}
.networks{top:652px;font-weight:700;font-size:8.4px;color:var(--paper)}
.networks span{margin:0 4px}
.networks span::before{content:"";display:inline-block;width:9px;height:9px;background:var(--paper);margin-right:3px;vertical-align:-1px}
.back-social{top:676px;color:var(--navy-deep)}
.back-social .lead{color:var(--navy-deep)}
.cert{top:742px;font-weight:700;font-size:8.4px;line-height:11px;color:var(--paper)}
</style>
</head>
<body>

<section class="flyer flyer--front" aria-label="Flyer front">
  <svg class="art" viewBox="0 0 377 775" aria-hidden="false">
    <defs>
      <linearGradient id="sky" x1="0" y1="0" x2="0" y2="1"><stop offset="0" stop-color="#5d93d6"/><stop offset=".6" stop-color="#b8cde0"/><stop offset="1" stop-color="#8f9b73"/></linearGradient>
      <linearGradient id="navyFade" x1="0" y1="0" x2="0" y2="1"><stop offset="0" stop-color="#1d2a66"/><stop offset="1" stop-color="#2a3b86"/></linearGradient>
      <linearGradient id="gold" x1="0" y1="0" x2="1" y2="0"><stop offset="0" stop-color="#b07d12"/><stop offset=".5" stop-color="#f1d272"/><stop offset="1" stop-color="#b98714"/></linearGradient>
      <linearGradient id="scene" x1="0" y1="0" x2="0" y2="1"><stop offset="0" stop-color="#a9bcc7"/><stop offset=".45" stop-color="#c99a4a"/><stop offset="1" stop-color="#5f7f48"/></linearGradient>
      <linearGradient id="mist" x1="0" y1="0" x2="0" y2="1"><stop offset="0" stop-color="#f3f4f7"/><stop offset="1" stop-color="#d9dde6"/></linearGradient>
    </defs>
    <rect width="377" height="300" fill="url(#sky)" role="img" aria-label="Photo: hot-air balloons over a misty valley at dawn"/>
    <rect y="270" width="377" height="225" fill="url(#navyFade)"/>
    <rect y="490" width="377" height="285" fill="url(#mist)"/>
    <path d="M0 492 Q188 462 377 492 L377 500 Q188 474 0 500 Z" fill="url(#gold)"/>
    <ellipse cx="188" cy="245" rx="184" ry="128" fill="url(#gold)"/>
    <ellipse cx="188" cy="240" rx="178" ry="120" fill="var(--paper)"/>
    <ellipse cx="186" cy="240" rx="170" ry="113" fill="#111"/>
    <ellipse cx="186" cy="240" rx="163" ry="107" fill="url(#scene)" role="img" aria-label="Photo: passengers in a balloon basket over a river at sunrise"/>
    <path d="M36 655 Q36 640 52 640 L325 640 Q341 640 341 655 L341 750 L36 750 Z" fill="url(#gold)"/>
    <path d="M0 740 Q188 705 377 740 L377 775 L0 775 Z" fill="var(--paper)"/>
    <path d="M0 748 Q188 716 377 748 L377 775 L0 775 Z" fill="var(--navy)"/>
  </svg>

  <h1 class="text headline">KING VALLEY HOT-AIR BALLOONING</h1>
  <h2 class="text subhead">THE PERFECT GOURMET<br>BALLOONING EXPERIENCE</h2>

  <div class="text intro">
    <p>Live the romance and adventure of flying the beautiful King Valley and surrounds in a hot-air balloon at dawn<br>From the vineyards and patchwork of fields the views expand to the Ovens River, spectacular Mt Buffalo and the High Country beyond<br>The mountain views, once aloft, come to life in dramatic 3D with the early morning light</p>
    <p>Celebrate your flight with a delicious breakfast afterwards (optional)</p>
    <p>Milawa is conveniently located less than an hour's drive from most places in Victoria's North East and Albury in NSW<br>Mansfield flights are also available</p>
  </div>

  <p class="text booking front-booking">FOR BOOKINGS OR MORE INFORMATION:</p>
  <p class="text contact front-contact"><span>www.skylarkaerialtours.com.au</span><br><span>flights@skylarkaerialtours.com.au</span><br><span>or call our friendly team on 1300 555 019</span></p>
  <p class="text social front-social"><span class="lead">Find us also on Chatterly, Snapframe and TripRate</span><br>@skylarkaerialtours</p>
</section>

<section class="flyer flyer--back" aria-label="Flyer back">
  <svg class="art" viewBox="0 0 377 775">
    <defs>
      <linearGradient id="skyBack" x1="0" y1="0" x2="0" y2="1"><stop offset="0" stop-color="#2f7fcf"/><stop offset=".55" stop-color="#a9c9e6"/><stop offset="1" stop-color="#ffffff"/></linearGradient>
      <linearGradient id="goldBack" x1="0" y1="0" x2="1" y2="0"><stop offset="0" stop-color="#b07d12"/><stop offset=".5" stop-color="#f1d272"/><stop offset="1" stop-color="#b98714"/></linearGradient>
    </defs>
    <rect width="377" height="270" fill="url(#skyBack)" role="img" aria-label="Photo: colourful hot-air balloons above fog-covered vineyards"/>
    <path d="M30 605 Q30 585 50 585 L327 585 Q347 585 347 605 L347 740 L30 740 Z" fill="url(#goldBack)"/>
    <path d="M0 722 Q188 700 377 722 L377 775 L0 775 Z" fill="var(--paper)"/>
    <path d="M0 732 Q188 712 377 732 L377 775 L0 775 Z" fill="var(--navy)"/>
  </svg>

  <div class="flight-box"></div>
  <div class="pill">YOUR FLIGHT</div>

  <ul class="bullets bullets--main">
    <li>One-hour sunrise balloon flight in the spectacular King Valley region in North East Victoria</li>
    <li>Delicious champagne breakfast after the flight<br>(recommended option)</li>
    <li>Informative details throughout your experience with our locally The opportunity to be involved in the inflation and deflation process should you wish</li>
  </ul>
  <ul class="bullets bullets--facts">
    <li>Safe, friendly and professional</li>
    <li>The flight lasts approximately 1 hour</li>
    <li>The entire experience takes about 3-4 hours</li>
    <li>Suitable from age 7 to 97</li>
    <li>Gift Vouchers are also available</li>
    <li>Contact us for exclusive flight options at your custom location</li>
  </ul>

  <p class="text booking back-booking">FOR BOOKINGS OR MORE INFORMATION:</p>
  <p class="text contact back-contact"><span>www.skylarkaerialtours.com.au</span><br><span>flights@skylarkaerialtours.com.au</span><br><span>or call our friendly team on 1300 555 019</span></p>
  <p class="text networks"><span>Chatterly</span><span>Snapframe</span><span>TripRate</span></p>
  <p class="text social back-social"><span class="lead">Find us also on Chatterly, Snapframe and TripRate</span><br>@skylarkaerialtours</p>
  <p class="text cert">Skylark Aerial Tours operates under Air Operator's Certificate C481073-12<br>issued by the National Air Safety Office</p>
</section>

</body>
</html>
```